Brochure Lantern Ridge Advisory

need brochure to display my services. We are a business consulting firm focused on small to medium size business. We also do speaking engagements and trainings on leadership development as well as help local suppliers bring products to mark
et. I have some specific ideas regarding setup. Would like to follow color scheme of my logo and my business cards. Like the black background. Also with setup would like the following:
Cover - Logo and Mission statement
Back - Bio
Inside( fully opened brochure) array of services separated by catagory
inside flap - mission/vision/purpose
I will upload sketch of this as well as Mission/Vision/Purpose statements

Target Market(s)

small to medium size business owners
local vendors
any purveyor of services or goods

Industry/Entity Type

Business Consultant

Font styles to use
Serif

Requirements
Must have
• want to include the following:
• Logo
• contact information
• bio
• array of services
• mission/vision/purpose statement - to be added to files later today
Nice to have
• Cover: Logo, Mission statement
• Back : Bio
• Inside: array of services on 3 inside pages; broken out onto 3 categories, 1 per page.
• will upload sketch of this

```html
<!DOCTYPE html>
<html lang="en">
<head>
<meta charset="utf-8">
<title>Lantern Ridge Advisory – Trifold Brochure</title>
<link href="https://fonts.googleapis.com/css2?family=Roboto+Condensed:wght@400;700&family=Open+Sans:wght@400;600;700&display=swap" rel="stylesheet">
<style>
  :root{
    --ink:#111111;
    --ink-soft:#1c1c1c;
    --green:#7cb82f;
    --green-dark:#5e9420;
    --green-text:#9bd14a;
    --orange:#f07d14;
    --white:#ffffff;
    --paper:#ffffff;
    --photo-warm-a:#cbb59c;
    --photo-warm-b:#8d7a66;
    --photo-cool-a:#c9ccd0;
    --photo-cool-b:#7d8790;
  }
  *{box-sizing:border-box;margin:0;padding:0}
  html,body{width:887px;height:1200px;overflow:hidden;background:var(--paper)}
  body{position:relative;font-family:"Open Sans",Arial,sans-serif;color:var(--white)}
  .spread{position:absolute;left:14px;width:859px;display:grid;grid-template-columns:repeat(3,1fr);box-shadow:0 2px 6px rgba(0,0,0,.25)}
  .spread--outside{top:28px;height:545px}
  .spread--inside{top:615px;height:555px}
  .panel{position:relative;overflow:hidden;background:var(--ink)}
  .photo{position:absolute;left:0;right:0;top:0}
  .photo--warm{background:linear-gradient(135deg,var(--photo-warm-a),var(--photo-warm-b))}
  .photo--cool{background:linear-gradient(135deg,var(--photo-cool-a),var(--photo-cool-b))}
  .swoosh{position:absolute;left:0;width:100%;display:block}
  .heading{font-family:"Roboto Condensed",Arial,sans-serif;font-weight:700;text-transform:uppercase;color:var(--orange);letter-spacing:.5px}
  .copy{font-size:7.6px;line-height:1.45;color:var(--white)}
  .copy--green{color:var(--green-text)}
  .block{position:absolute;left:22px;right:22px}
  .block .heading{font-size:12px;margin-bottom:4px;padding-bottom:3px;border-bottom:1px solid var(--green)}
  .portrait{position:absolute;border-radius:50%;border:4px solid var(--green);background:linear-gradient(135deg,var(--photo-warm-a),var(--photo-warm-b))}
  .bio p+p{margin-top:7px}
  .brand{position:absolute;left:0;right:0;text-align:center;display:flex;align-items:center;justify-content:center;gap:8px}
  .brand__dot{width:12px;height:12px;border-radius:50%;background:var(--white)}
  .brand__name{font-size:15px;font-weight:700;text-transform:uppercase;letter-spacing:1px;color:var(--white);line-height:1.1}
  .tagline{position:absolute;left:0;right:0;text-align:center}
  .tagline__bar{background:var(--orange);color:var(--white);font-family:"Roboto Condensed",Arial,sans-serif;font-weight:700;font-size:19px;padding:6px 0;text-transform:uppercase}
  .tagline__sub{color:var(--orange);font-size:8px;font-weight:700;text-transform:uppercase;margin-top:6px;letter-spacing:.4px}
  .list{display:grid;grid-template-columns:1fr 1fr;column-gap:10px;list-style:none;font-size:8.4px;line-height:1.75}
  .list li::before{content:"";display:inline-block;width:4px;height:4px;background:var(--orange);margin-right:5px;vertical-align:middle}
  .list--green li{color:var(--green-text)}
  .section-tab{display:inline-block;background:var(--orange);color:var(--white);font-family:"Roboto Condensed",Arial,sans-serif;font-weight:700;font-size:12px;padding:4px 10px;text-transform:uppercase}
  .green-field{position:absolute;left:0;right:0;background:var(--green)}
</style>
</head>
<body>

<!-- Outside spread -->
<section class="spread spread--outside">
  <!-- Inside flap: mission / purpose / vision -->
  <article class="panel">
    <div class="photo photo--warm" style="height:215px" role="img" aria-label="Photo of a smiling shop owner holding an open sign in a storefront"></div>
    <svg class="swoosh" style="top:180px;height:70px" viewBox="0 0 286 70" preserveAspectRatio="none" aria-hidden="true">
      <path d="M0 30 Q140 0 286 20 L286 70 L0 70Z" fill="var(--orange)"/>
      <path d="M0 40 Q140 12 286 32 L286 70 L0 70Z" fill="var(--green)"/>
      <path d="M0 52 Q150 28 286 46 L286 70 L0 70Z" fill="var(--ink)"/>
    </svg>
    <div class="block" style="top:258px">
      <h2 class="heading">Mission</h2>
      <p class="copy copy--green">To encourage and support the growth of small to medium size businesses through guidance, training and practical tools that build lasting success.</p>
    </div>
    <div class="block" style="top:338px">
      <h2 class="heading">Purpose</h2>
      <p class="copy copy--green">We partner with owners and local vendors to sharpen strategy, strengthen teams and bring quality products to market with confidence.</p>
    </div>
    <div class="block" style="top:418px">
      <h2 class="heading">Vision</h2>
      <p class="copy copy--green">A thriving local economy where every business owner has the knowledge, network and support needed to grow.</p>
    </div>
  </article>

  <!-- Back: bio -->
  <article class="panel">
    <svg class="swoosh" style="top:0;height:60px" viewBox="0 0 286 60" preserveAspectRatio="none" aria-hidden="true">
      <path d="M0 0 L286 0 L286 24 Q150 50 0 30Z" fill="var(--green)"/>
      <path d="M0 30 Q150 50 286 24 L286 30 Q150 58 0 36Z" fill="var(--orange)"/>
    </svg>
    <div class="portrait" style="left:108px;top:12px;width:70px;height:70px" role="img" aria-label="Round portrait of the firm's founder"></div>
    <div class="block bio" style="top:98px">
      <h2 class="heading" style="border:none;text-align:center;font-size:13px">Meet Our Founder</h2>
      <p class="copy">With more than twenty years leading retail and service teams, our founder has helped owners turn ideas into profitable, well run companies.</p>
      <p class="copy">Lantern Ridge Advisory was built to give small and medium size businesses the same strategic support larger firms rely on every day.</p>
      <p class="copy">Today the firm offers consulting, training and speaking engagements focused on leadership, growth and bringing local products to market.</p>
    </div>
    <svg class="swoosh" style="bottom:0;height:90px" viewBox="0 0 286 90" preserveAspectRatio="none" aria-hidden="true">
      <path d="M0 40 Q150 10 286 30 L286 90 L0 90Z" fill="var(--orange)"/>
      <path d="M0 52 Q150 24 286 44 L286 90 L0 90Z" fill="var(--green)"/>
    </svg>
  </article>

  <!-- Cover -->
  <article class="panel">
    <div class="photo photo--cool" style="height:245px" role="img" aria-label="Photo of a business owner on the phone at his desk"></div>
    <svg class="swoosh" style="top:200px;height:60px" viewBox="0 0 286 60" preserveAspectRatio="none" aria-hidden="true">
      <path d="M0 40 Q150 0 286 22 L286 60 L0 60Z" fill="var(--orange)"/>
      <path d="M0 48 Q150 10 286 32 L286 60 L0 60Z" fill="var(--green)"/>
    </svg>
    <div class="green-field" style="top:258px;height:110px"></div>
    <div class="brand" style="top:290px">
      <span class="brand__dot"></span>
      <span class="brand__name">Lantern Ridge<br>Advisory</span>
    </div>
    <div class="tagline" style="top:385px">
      <div class="tagline__bar">To Encourage and Support</div>
      <div class="tagline__sub">The growth of small to medium size business</div>
    </div>
    <div class="green-field" style="bottom:0;height:38px"></div>
  </article>
</section>

<!-- Inside spread -->
<section class="spread spread--inside">
  <article class="panel">
    <div class="photo photo--warm" style="height:300px" role="img" aria-label="Photo of a businesswoman smiling at her desk"></div>
    <svg class="swoosh" style="top:270px;height:60px" viewBox="0 0 286 60" preserveAspectRatio="none" aria-hidden="true">
      <path d="M0 20 Q150 48 286 18 L286 60 L0 60Z" fill="var(--orange)"/>
      <path d="M0 30 Q150 58 286 28 L286 60 L0 60Z" fill="var(--green)"/>
      <path d="M0 40 Q150 64 286 38 L286 60 L0 60Z" fill="var(--ink)"/>
    </svg>
    <div class="block" style="top:352px">
      <h2 class="section-tab" style="margin-bottom:10px">Products to Market</h2>
      <ul class="list list--green">
        <li>Product Development</li><li>Logistics</li>
        <li>Business Plan</li><li>Merchandising</li>
        <li>Marketing</li><li>Distribution</li>
        <li>Vendor Relations</li><li>Placement</li>
      </ul>
    </div>
  </article>

  <article class="panel">
    <div class="green-field" style="top:0;height:230px"></div>
    <svg class="swoosh" style="top:200px;height:60px" viewBox="0 0 286 60" preserveAspectRatio="none" aria-hidden="true">
      <path d="M0 10 Q150 50 286 20 L286 60 L0 60Z" fill="var(--orange)"/>
      <path d="M0 20 Q150 60 286 30 L286 60 L0 60Z" fill="var(--ink)"/>
    </svg>
    <div class="portrait" style="left:100px;top:140px;width:86px;height:86px;background:linear-gradient(135deg,var(--photo-cool-a),var(--photo-warm-b))" role="img" aria-label="Round photo of a storefront exterior"></div>
    <div class="block" style="top:290px">
      <h2 class="section-tab" style="margin-bottom:10px">Business Support</h2>
      <ul class="list">
        <li>Start Up</li><li>Profitability</li>
        <li>Business Plan</li><li>Training &amp; Development</li>
        <li>Marketing Strategies</li><li>Recruiting &amp; Hiring</li>
        <li>Merchandising</li><li>Mentoring</li>
        <li>Customer Experience</li><li>Research &amp; Development</li>
        <li>Sales Growth</li>
      </ul>
    </div>
    <svg class="swoosh" style="bottom:0;height:50px" viewBox="0 0 286 50" preserveAspectRatio="none" aria-hidden="true">
      <path d="M0 30 Q150 0 286 20 L286 50 L0 50Z" fill="var(--green)"/>
    </svg>
  </article>

  <article class="panel">
    <div class="photo photo--cool" style="height:310px" role="img" aria-label="Photo of a consultant in glasses working on a laptop"></div>
    <svg class="swoosh" style="top:280px;height:60px" viewBox="0 0 286 60" preserveAspectRatio="none" aria-hidden="true">
      <path d="M0 18 Q150 46 286 16 L286 60 L0 60Z" fill="var(--orange)"/>
      <path d="M0 28 Q150 56 286 26 L286 60 L0 60Z" fill="var(--green)"/>
      <path d="M0 38 Q150 62 286 36 L286 60 L0 60Z" fill="var(--ink)"/>
    </svg>
    <div class="block" style="top:345px">
      <h2 class="heading">Lectures &amp; Seminars</h2>
      <ul class="list list--green" style="margin-bottom:12px">
        <li>Trainings</li><li>Workshops</li>
      </ul>
      <h2 class="heading">Leadership Development</h2>
      <p class="copy copy--green">We help leaders build stronger teams through coaching, practical workshops and clear goals. Sessions are tailored to your people, your market and the results you want to achieve.</p>
    </div>
    <div class="green-field" style="bottom:0;height:10px;background:var(--orange)"></div>
  </article>
</section>

</body>
</html>
```